SaaS Early tech startup business card design

Unique design for experience ecommerce platform company. the business cards will be used by executive members. conformance with color code is required.

```html
<!DOCTYPE html>
<html lang="en">
<head>
<meta charset="utf-8">
<title>Novra Business Card</title>
<link rel="stylesheet" href="https://fonts.googleapis.com/css2?family=Lato:wght@400;700;900&display=swap">
<style>
  :root {
    --stage: #a3a3a3;
    --paper: #ffffff;
    --navy-teal: #07648f;
    --mid-teal: #0a8a9c;
    --sea-green: #02b39a;
    --brand-teal: #0e9a9a;
    --ink: #222222;
    --rule: #8c8c8c;
  }
  * { box-sizing: border-box; margin: 0; padding: 0; }
  html, body {
    width: 1200px; height: 1200px; overflow: hidden;
    background: var(--stage);
    font-family: "Lato", sans-serif;
  }
  .canvas { position: relative; width: 1200px; height: 1200px; }

  .card {
    position: absolute; top: 303px; width: 370px; height: 594px;
    box-shadow: 3px 4px 6px rgba(0,0,0,0.45);
  }
  .card--front { left: 200px; }
  .card--back { left: 599px; background: var(--paper); }

  .front-field {
    position: absolute; inset: 0;
    background: linear-gradient(180deg, var(--navy-teal) 0%, var(--mid-teal) 45%, var(--sea-green) 100%);
  }

  .wordmark {
    position: absolute; left: 0; right: 0; text-align: center;
    font-weight: 900; letter-spacing: 1px; line-height: 1;
  }
  .card--front .wordmark { top: 540px; top: 232px; font-size: 96px; color: var(--paper); }
  .card--back .wordmark { top: 115px; font-size: 96px; color: var(--brand-teal); }

  .identity { position: absolute; top: 337px; left: 0; right: 0; text-align: center; }
  .identity__name {
    font-weight: 700; font-size: 25px; color: var(--brand-teal); letter-spacing: 0.5px; line-height: 1;
  }
  .identity__title { font-size: 17px; color: var(--ink); margin-top: 6px; }

  .icon-row {
    position: absolute; top: 394px; left: 87px; right: 87px;
    display: flex; align-items: center; gap: 5px;
  }
  .icon-row__rule { flex: 1; height: 1px; background: var(--rule); }
  .icon-row__rule:first-child { margin-right: 3px; }
  .icon-row__rule:last-child { margin-left: 3px; }
  .icon { width: 25px; height: 25px; border-radius: 3px; background: var(--brand-teal); display: flex; align-items: center; justify-content: center; }

  .contact { position: absolute; top: 432px; left: 0; right: 0; text-align: center; font-size: 17px; color: var(--ink); line-height: 22px; }
  .divider { position: absolute; top: 507px; left: 88px; right: 81px; height: 1px; background: var(--rule); }
  .address { position: absolute; top: 518px; left: 0; right: 0; text-align: center; font-size: 17px; color: var(--ink); line-height: 22px; }
</style>
</head>
<body>
<main class="canvas">
  <section class="card card--front">
    <div class="front-field" role="img" aria-label="Blue to teal gradient with a decorative pattern of stacked square tiles"></div>
    <div class="wordmark">novra</div>
  </section>

  <section class="card card--back">
    <div class="wordmark">novra</div>

    <div class="identity">
      <p class="identity__name">DANIEL CARTER</p>
      <p class="identity__title">Managing Director</p>
    </div>

    <div class="icon-row">
      <span class="icon-row__rule"></span>
      <span class="icon" aria-label="Phone">
        <svg width="17" height="15" viewBox="0 0 17 15"><path d="M1 5 Q8.5 0 16 5 L14 7 L11.5 5.5 L11.5 4 Q8.5 3 5.5 4 L5.5 5.5 L3 7 Z" fill="#fff"/><rect x="4" y="8" width="9" height="6" rx="1" fill="#fff"/></svg>
      </span>
      <span class="icon" aria-label="Email">
        <svg width="17" height="13" viewBox="0 0 17 13"><rect x="1" y="1" width="15" height="11" fill="none" stroke="#fff" stroke-width="1.4"/><path d="M1 1 L8.5 7.5 L16 1 M1 12 L6.5 6 M16 12 L10.5 6" fill="none" stroke="#fff" stroke-width="1.2"/></svg>
      </span>
      <span class="icon" aria-label="Website">
        <svg width="17" height="17" viewBox="0 0 17 17"><circle cx="8.5" cy="8.5" r="7" fill="none" stroke="#fff" stroke-width="1.4"/><ellipse cx="8.5" cy="8.5" rx="3" ry="7" fill="none" stroke="#fff" stroke-width="1.1"/><path d="M1.5 8.5 H15.5" stroke="#fff" stroke-width="1.1"/></svg>
      </span>
      <span class="icon-row__rule"></span>
    </div>

    <div class="contact">
      <p>055-246 813 579</p>
      <p>hello@novrashop.com</p>
      <p>www.novrashop.com</p>
    </div>

    <div class="divider"></div>

    <div class="address">
      <p>88, Harbor Lane West</p>
      <p>20417, Eastland</p>
    </div>
  </section>
</main>
</body>
</html>
```